Real Estate Company Needs a Contemporary/Modern Business Card Design

We need a Contemporary/Modern Business Card Design for a New Real Estate Company based in San Francisco, CA called Colvane Terrish Realtors. We would like to see designs that use the color red for the "Colvane Terrish" and gold for the "Realtors." The design should communicate being Modern and yet Established and Stable.

Industry/Entity Type

Business

```html
<!DOCTYPE html>
<html lang="en">
<head>
<meta charset="utf-8">
<title>Colvane Terrish Realtors Business Card</title>
<link rel="stylesheet" href="https://fonts.googleapis.com/css2?family=Abril+Fatface&family=Old+Standard+TT:wght@400;700&family=Questrial&display=swap">
<style>
  :root {
    --paper: #ffffff;
    --red-deep: #9c0a17;
    --red: #cc2027;
    --red-ink: #b3151f;
    --gold: #c9932a;
    --ink: #222222;
    --muted: #444444;
    --shadow: 0 3px 8px rgba(0,0,0,0.28);
  }
  * { margin: 0; padding: 0; box-sizing: border-box; }
  html, body { width: 1200px; height: 828px; overflow: hidden; background: var(--paper); }
  .board { position: relative; width: 1200px; height: 828px; background: var(--paper); }

  .card { position: absolute; width: 319px; height: 195px; box-shadow: var(--shadow); overflow: hidden; }
  .card--deep { background: var(--red-deep); }
  .card--red { background: var(--red); }
  .card--white { background: var(--paper); }

  .wordmark { font-family: "Abril Fatface", serif; font-weight: 400; color: var(--paper); line-height: 0.95; white-space: nowrap; }
  .card--white .wordmark { color: var(--red); }
  .wordmark--gold { color: var(--gold) !important; }

  .tagline { font-family: "Old Standard TT", serif; font-weight: 700; color: var(--gold); font-size: 13px; letter-spacing: 1px; }
  .tagline--wide { font-size: 11px; letter-spacing: 4px; }
  .rule { position: absolute; height: 1.5px; width: 20px; background: var(--gold); }

  .contact { position: absolute; font-family: "Old Standard TT", serif; font-size: 11px; line-height: 13.5px; color: var(--muted); letter-spacing: 0.5px; }
  .contact .agent { color: var(--red-ink); font-weight: 700; }

  .centered { position: absolute; left: 0; right: 0; text-align: center; }
  .abs { position: absolute; }

  .label { position: absolute; font-family: "Questrial", sans-serif; font-size: 14px; color: #111; }
  .sheet-title { position: absolute; left: 124px; top: 690px; font-family: "Questrial", sans-serif; font-size: 22px; color: #111; }
  .sheet-rule { position: absolute; left: 124px; top: 735px; width: 960px; height: 1.5px; background: #111; }
  .sheet-client { position: absolute; left: 124px; top: 747px; font-family: "Questrial", sans-serif; font-size: 15px; color: #111; }
</style>
</head>
<body>
<main class="board">

  <!-- Front, centered -->
  <section class="card card--deep" style="left:85px; top:105px;">
    <div class="centered wordmark" style="top:70px; font-size:28px;">Colvane Terrish</div>
    <div class="rule" style="left:150px; top:111px;"></div>
    <div class="centered tagline" style="top:121px;">REALTORS.</div>
  </section>
  <p class="label" style="left:90px; top:327px;">FRONT</p>

  <!-- Front, stacked -->
  <section class="card card--red" style="left:459px; top:105px;">
    <div class="abs wordmark" style="left:30px; top:24px; font-size:39px;">Colvane<br>Terrish.</div>
    <div class="rule" style="left:31px; top:102px;"></div>
    <div class="abs tagline tagline--wide" style="left:31px; top:111px;">REALTORS</div>
    <div class="rule" style="left:31px; top:134px;"></div>
  </section>
  <p class="label" style="left:460px; top:327px;">FRONT</p>

  <!-- Front, three lines -->
  <section class="card card--red" style="left:836px; top:109px;">
    <div class="abs wordmark" style="left:30px; top:22px; font-size:39px;">Colvane<br>Terrish</div>
    <div class="abs wordmark wordmark--gold" style="left:30px; top:96px; font-size:39px;">Realtors.</div>
    <div class="rule" style="left:33px; top:142px; width:30px;"></div>
  </section>
  <p class="label" style="left:838px; top:327px;">FRONT</p>

  <!-- Back, centered -->
  <section class="card card--white" style="left:87px; top:392px;">
    <div class="centered wordmark" style="top:42px; font-size:28px; color:var(--red-ink);">Colvane Terrish</div>
    <div class="rule" style="left:150px; top:82px;"></div>
    <div class="centered tagline" style="top:90px; color:#b8862a;">REALTORS.</div>
    <div class="centered contact" style="top:142px;"><span class="agent">CT Terrish</span>&nbsp; (415) 555-0182</div>
    <div class="centered contact" style="top:158px;">1840 Harlow Court, Daly City, CA 94014</div>
  </section>
  <p class="label" style="left:92px; top:615px;">BACK</p>

  <!-- Back, stacked -->
  <section class="card card--white" style="left:457px; top:393px;">
    <div class="abs wordmark" style="left:17px; top:25px; font-size:27px;">Colvane<br>Terrish.</div>
    <div class="rule" style="left:18px; top:84px;"></div>
    <div class="abs tagline tagline--wide" style="left:18px; top:91px; font-size:9px;">REALTORS</div>
    <div class="rule" style="left:18px; top:109px;"></div>
    <div class="contact" style="left:182px; top:119px;">
      <span class="agent">CT Terrish</span><br>(415) 555-0182<br>1840 Harlow Court<br>Daly City, CA 94014
    </div>
  </section>
  <p class="label" style="left:464px; top:615px;">BACK</p>

  <!-- Back, three lines -->
  <section class="card card--white" style="left:837px; top:397px;">
    <div class="abs wordmark" style="left:18px; top:20px; font-size:27px;">Colvane<br>Terrish</div>
    <div class="abs wordmark wordmark--gold" style="left:18px; top:72px; font-size:27px;">Realtors.</div>
    <div class="rule" style="left:19px; top:110px; width:32px;"></div>
    <div class="contact" style="left:191px; top:121px;">
      <span class="agent">CT Terrish</span><br>(415) 555-0182<br>1840 Harlow Court<br>Daly City, CA 94014
    </div>
  </section>
  <p class="label" style="left:842px; top:615px;">BACK</p>

  <h1 class="sheet-title" style="font-weight:400;">Colvane Terrish Realtors Business Card</h1>
  <div class="sheet-rule"></div>
  <p class="sheet-client">Client: Colvane Terrish Realtors</p>

</main>
</body>
</html>
```